Website re-design wedding music business

I need my wordpress wedding music website redesigned. I'm a wedding pianist and also provide duo/trio entertainment with other musicians and looking for an overhaul of my wordpress site.

Website: tomaslevett.com.au

Target Market(s)

brides; engaged couples

Industry/Entity Type

Wedding

Number of Pages Required

5+ page

Colors

Designer to choose colors to be used in the design.

Requirements
Must have
• I'm looking to overhaul my website which is looking rather tired after 4 years. It is functional but not inviting to visitors. Initially my website started out as a solo piano player providing music for wedding. It is gradually growing now where brides can book
• 1) Solo Piano
• 2) Duo (any combination of Piano / Cello / Vocalist / Violin)
• 3) Trio (any combination of Piano/ Cello /Vocalist / Violin)
• in future it may increase to 4 / 5 /6 piece bands so that needs to be taken into account for the future growth where I'll recruit other musicians.
• Some other functionality I'd like to see
• - Visitors want a calendar to know availability of musicians
• - Automatically providing enquiry price & discount (if applicable)
• - Automating the booking form process (manual) - There's a PDF form I send to the customer after we go back/forth on email on songs/price etc but if more of it could be automated online that would be great. If move to online it would be good to be able to override the set prices with a custom price and also providing a payment gateway
• More Flexibility on pricing - customer selects type of artists they want and it calculates a price based on who they have chosen whether it is a ceremony or canapes or reception (or combination of any). Extra transport fee is added if >50km out of Melbourne.
• How would you re-design this website. Imagine you are a bride/groom looking to book wedding music services. I would love to see some concepts .
• Please indicate any other fees required for your submission and level of support post this competition. I would like this to be an on-going relationship.
Nice to have
• I'd preferably like the website to be in wordpress as I've been familiar with it over time and can do basic updates in the back end. Happy for other suggestions if you can convince me I should move away from wordpress.

```html
<!DOCTYPE html>
<html lang="en">
<head>
<meta charset="utf-8">
<title>Elliot Hale – Wedding Pianist Melbourne</title>
<link rel="stylesheet" href="https://fonts.googleapis.com/css2?family=Montserrat:wght@400;600;700&family=Open+Sans:wght@400;600;700&display=swap">
<style>
:root{
  --ink:#1c1c1c;
  --text:#555;
  --muted:#8a8a8a;
  --line:#d6d6d6;
  --paper:#ffffff;
  --mist:#efefef;
  --dark:#2b2b2b;
  --black:#111;
  --hero-a:#3a3f3a;
  --hero-b:#111413;
}
*{box-sizing:border-box;margin:0;padding:0}
html,body{width:1200px;height:3132px;overflow:hidden}
body{background:var(--paper);font-family:"Open Sans",Arial,sans-serif;color:var(--text);font-size:15px;position:relative}
h1,h2,h3,h4{font-family:"Montserrat",Arial,sans-serif;color:var(--ink);font-weight:700;text-transform:uppercase}
.btn{display:inline-block;border:2px solid var(--ink);color:var(--ink);font:700 12px "Montserrat",sans-serif;letter-spacing:1px;text-transform:uppercase;padding:10px 22px;background:transparent}
.btn--light{border-color:#fff;color:#fff}

/* Hero */
.hero{position:absolute;left:0;top:0;width:1200px;height:640px;overflow:hidden}
.hero__photo{position:absolute;inset:0;background:radial-gradient(ellipse at 35% 45%,#5b5f57 0%,var(--hero-a) 35%,var(--hero-b) 100%)}
.hero__shade{position:absolute;inset:0;background:linear-gradient(180deg,rgba(0,0,0,.45) 0%,rgba(0,0,0,.1) 30%,rgba(0,0,0,.35) 100%)}
.topbar{position:absolute;top:8px;right:40px;display:flex;gap:14px;align-items:center;font-size:12px;color:#ddd}
.topbar span.sep{color:#888}
.topbar .dots{display:flex;gap:6px;margin-left:8px}
.topbar .dots i{width:16px;height:16px;border-radius:50%;background:#bbb;display:block}
.brand{position:absolute;left:110px;top:40px;display:flex;align-items:center;gap:10px;font:700 22px "Montserrat",sans-serif;color:#fff;text-transform:uppercase;letter-spacing:1px}
.brand .mark{width:34px;height:34px;border-radius:50%;background:#fff}
.nav{position:absolute;right:120px;top:56px;display:flex;gap:26px;font:600 14px "Open Sans",sans-serif;color:#fff}
.nav a{color:#fff;text-decoration:none;padding-bottom:6px}
.nav a.active{border-bottom:2px solid #fff}
.hero__title{position:absolute;top:282px;width:100%;text-align:center;color:#fff;font-size:44px;letter-spacing:1px}
.hero__lead{position:absolute;top:344px;left:330px;width:540px;text-align:center;color:#eee;font-size:15px;line-height:1.55}
.hero__cta{position:absolute;top:420px;left:0;width:100%;text-align:center}
.arrow{position:absolute;top:318px;width:44px;height:44px;border-radius:50%;border:2px solid #fff;display:flex;align-items:center;justify-content:center}
.arrow--l{left:92px}.arrow--r{right:92px}

/* Services */
.services{position:absolute;top:0;left:0;width:1200px;height:1000px}
.services__wave{position:absolute;left:0;top:640px;width:1200px;height:340px;background:var(--mist)}
.services__wave svg{position:absolute;bottom:-1px;left:0}
.service{position:absolute;top:590px;width:300px;height:300px;border-radius:50%;background:var(--black);color:#fff;text-align:center;padding-top:58px;border:8px solid #fff;box-shadow:0 0 0 1px #ccc}
.service__icon{height:44px;display:flex;align-items:flex-end;justify-content:center}
.service h3{color:#fff;font-size:22px;margin:12px 0 10px}
.service p{font-size:12px;line-height:1.45;color:#ccc;width:190px;height:54px;margin:0 auto 12px}
.service--solo{left:150px}
.service--duo{left:450px;background:#fff;color:var(--ink);border-color:#e8e8e8}
.service--duo h3{color:var(--ink)}
.service--duo p{color:var(--muted)}
.service--trio{left:750px}
.service .btn{font-size:10px;padding:7px 16px}

/* About */
.about{position:absolute;top:1030px;left:110px;width:980px;height:380px}
.about h2{font-size:36px;margin-bottom:24px}
.about p{font-size:14px;line-height:1.75;width:540px;margin-bottom:14px}
.about .btn{margin-top:8px}
.calendar{position:absolute;right:0;top:20px;width:300px;border:1px solid var(--line);font-size:13px}
.calendar__head{background:var(--dark);color:#fff;display:flex;justify-content:space-between;padding:12px 16px;font:700 14px "Montserrat",sans-serif}
.calendar table{width:100%;border-collapse:collapse;text-align:center}
.calendar th{background:#6a6a6a;color:#fff;font-weight:600;font-size:12px;padding:6px 0}
.calendar td{padding:8px 0;border:1px solid #eee;color:#444}
.calendar td.off{color:#bbb}
.calendar td.today{background:var(--black);color:#fff;font-weight:700}

/* Music */
.music{position:absolute;top:1440px;left:0;width:1200px;height:490px;background:linear-gradient(180deg,#3c3c3c,#262626)}
.music h2{color:#fff;text-align:center;font-size:30px;padding-top:50px}
.tracks{position:absolute;top:120px;left:110px;width:980px;display:flex;gap:20px}
.track{flex:1;height:210px;background:rgba(0,0,0,.35);border:1px solid rgba(255,255,255,.15)}
.track__wave{height:110px;background:linear-gradient(180deg,#4a4a4a,#1c1c1c)}
.track__info{display:flex;gap:10px;padding:14px 12px;color:#ddd;font-size:11px;line-height:1.45}
.track__play{width:30px;height:30px;border-radius:50%;border:2px solid #fff;flex:none;display:flex;align-items:center;justify-content:center}
.track__info b{display:block;color:#fff;font-size:13px;font-weight:600}
.music__more{position:absolute;top:402px;width:100%;text-align:center}

/* Events */
.events{position:absolute;top:1960px;left:110px;width:980px;height:300px}
.events h2{text-align:center;font-size:30px;margin-bottom:44px}
.event-list{display:flex;gap:40px}
.event{flex:1;display:flex;gap:14px}
.event__date{width:70px;height:76px;border:2px solid var(--ink);text-align:center;flex:none}
.event__date b{display:block;font:700 30px "Montserrat",sans-serif;color:var(--ink);line-height:44px}
.event__date span{font-size:12px;text-transform:uppercase;color:var(--muted)}
.event h4{font-size:14px;text-transform:none;margin-bottom:6px;line-height:1.3}
.event small{display:block;font-size:11px;color:var(--muted);margin-bottom:6px}
.event p{font-size:11px;line-height:1.5}
.slider-dots{display:flex;justify-content:center;gap:8px;margin-top:44px}
.slider-dots i{width:30px;height:4px;background:#ccc;display:block}
.slider-dots i.on{background:var(--ink)}

/* Testimonials */
.testimonials{position:absolute;top:2270px;left:0;width:1200px;height:400px;background:var(--mist)}
.testimonials h2{text-align:center;font-size:30px;padding-top:60px}
.quote-badge{position:absolute;top:120px;left:570px;width:60px;height:60px;border-radius:50%;background:var(--black);display:flex;align-items:center;justify-content:center;z-index:2}
.quote-box{position:absolute;top:150px;left:230px;width:740px;height:190px;border:2px solid #bbb;text-align:center;padding:48px 50px 0;font-style:italic;font-size:14px;line-height:1.7}
.quote-box cite{display:block;margin-top:12px;font:700 12px "Montserrat",sans-serif;font-style:normal;color:var(--ink);text-transform:uppercase}
.t-arrow{position:absolute;top:230px}
.t-arrow--l{left:150px}.t-arrow--r{right:150px}

/* Footer */
.footer{position:absolute;top:2800px;left:160px;width:880px;display:flex;justify-content:space-between}
.footer h4{font-size:15px;margin-bottom:16px}
.footer ul{list-style:none;font-size:13px;line-height:2.1}
.socials{display:flex;gap:8px;margin-bottom:26px}
.socials i{width:30px;height:30px;border:2px solid var(--ink);border-radius:50%;display:block}
.footer .brand{position:static;color:var(--ink);font-size:18px}
.footer .brand .mark{width:28px;height:28px;background:var(--ink)}
.copyright{position:absolute;top:3070px;left:0;width:1200px;border-top:1px solid var(--line);text-align:center;padding-top:22px;font-size:11px;color:var(--muted)}
</style>
</head>
<body>

<header class="hero">
  <div class="hero__photo" role="img" aria-label="Pianist in a suit seated at a white grand piano beneath trees"></div>
  <div class="hero__shade"></div>
  <div class="topbar">
    <span>Testimonials</span><span class="sep">|</span><span>Buy CD</span><span class="sep">|</span><span>FAQs</span><span class="sep">|</span><span>Contact</span>
    <span class="dots"><i></i><i></i><i></i><i></i></span>
  </div>
  <div class="brand"><span class="mark"></span>Elliot Hale</div>
  <nav class="nav">
    <a class="active">Home</a><a>About Elliot</a><a>Events</a><a>Music</a><a>Video</a><a>Prices</a><a>Gallery</a>
  </nav>
  <a class="arrow arrow--l"><svg width="14" height="14" viewBox="0 0 14 14"><path d="M9 2 4 7l5 5" fill="none" stroke="#fff" stroke-width="2"/></svg></a>
  <a class="arrow arrow--r"><svg width="14" height="14" viewBox="0 0 14 14"><path d="M5 2l5 5-5 5" fill="none" stroke="#fff" stroke-width="2"/></svg></a>
  <h1 class="hero__title">Welcome to Elliot Hale</h1>
  <p class="hero__lead">Elliot Hale is Melbourne's premier award winning wedding &amp; event pianist specialising in playing beautiful background music for weddings.</p>
  <div class="hero__cta"><a class="btn btn--light">Book Now</a></div>
</header>

<section class="services">
  <div class="services__wave">
    <svg width="1200" height="80" viewBox="0 0 1200 80" preserveAspectRatio="none"><path d="M0 40 C200 0 400 80 600 40 S1000 0 1200 40 V80 H0Z" fill="#fff"/></svg>
  </div>
  <div class="service service--solo">
    <div class="service__icon"><svg width="56" height="40" viewBox="0 0 56 40"><path d="M4 36V20C4 8 18 4 30 8c8 3 10 10 22 10v18Z" fill="#fff"/></svg></div>
    <h3>Solo Piano</h3>
    <p>Elegant solo piano music for ceremonies, canapes and receptions.</p>
    <a class="btn btn--light">Learn More</a>
  </div>
  <div class="service service--duo">
    <div class="service__icon"><svg width="48" height="40" viewBox="0 0 48 40"><rect x="2" y="2" width="44" height="36" fill="none" stroke="#111" stroke-width="2"/><path d="M12 2v36M24 2v36M36 2v36" stroke="#111" stroke-width="2"/><path d="M9 2h6v20H9zM21 2h6v20h-6zM33 2h6v20h-6z" fill="#111"/></svg></div>
    <h3>Duo</h3>
    <p>Piano paired with cello, violin or vocals for your special day.</p>
    <a class="btn">Learn More</a>
  </div>
  <div class="service service--trio">
    <div class="service__icon"><svg width="40" height="44" viewBox="0 0 40 44"><ellipse cx="16" cy="30" rx="11" ry="12" fill="#fff"/><path d="M20 20 36 2" stroke="#fff" stroke-width="3"/></svg></div>
    <h3>Trio</h3>
    <p>Three musicians for a fuller sound at every part of the day.</p>
    <a class="btn btn--light">Learn More</a>
  </div>
</section>

<section class="about">
  <h2>About Elliot Hale</h2>
  <p>Elliot has played at hundreds of Melbourne weddings, bringing warm, graceful piano music to ceremonies, canapes and receptions across the city and regions.</p>
  <p>From classical pieces to modern love songs, every set list is shaped around the couple. Duo and trio options with cello, violin and vocals let you build the sound you want.</p>
  <a class="btn">Book Now</a>
  <div class="calendar">
    <div class="calendar__head"><span>‹</span><span>AUGUST 2017</span><span>›</span></div>
    <table>
      <tr><th>Su</th><th>Mo</th><th>Tu</th><th>We</th><th>Th</th><th>Fr</th><th>Sa</th></tr>
      <tr><td class="off">30</td><td class="off">31</td><td>1</td><td>2</td><td>3</td><td>4</td><td>5</td></tr>
      <tr><td>6</td><td>7</td><td>8</td><td>9</td><td>10</td><td>11</td><td>12</td></tr>
      <tr><td>13</td><td>14</td><td>15</td><td>16</td><td>17</td><td>18</td><td>19</td></tr>
      <tr><td class="today">20</td><td>21</td><td>22</td><td>23</td><td>24</td><td>25</td><td>26</td></tr>
      <tr><td>27</td><td>28</td><td>29</td><td>30</td><td>31</td><td class="off">1</td><td class="off">2</td></tr>
      <tr><td class="off">3</td><td class="off">4</td><td class="off">5</td><td class="off">6</td><td class="off">7</td><td class="off">8</td><td class="off">9</td></tr>
    </table>
  </div>
</section>

<section class="music" aria-label="Our Music">
  <h2>Our Music</h2>
  <div class="tracks">
    <div class="track"><div class="track__wave" role="img" aria-label="Audio waveform"></div><div class="track__info"><span class="track__play"><svg width="10" height="12"><path d="M1 1l8 5-8 5z" fill="#fff"/></svg></span><div><b>Music Title here</b>Short piece for a ceremony entrance<br>3:45</div></div></div>
    <div class="track"><div class="track__wave" role="img" aria-label="Audio waveform"></div><div class="track__info"><span class="track__play"><svg width="10" height="12"><path d="M1 1l8 5-8 5z" fill="#fff"/></svg></span><div><b>Music Title here</b>Gentle melody for signing the register<br>4:10</div></div></div>
    <div class="track"><div class="track__wave" role="img" aria-label="Audio waveform"></div><div class="track__info"><span class="track__play"><svg width="10" height="12"><path d="M1 1l8 5-8 5z" fill="#fff"/></svg></span><div><b>Music Title here</b>Light background music for canapes<br>3:20</div></div></div>
    <div class="track"><div class="track__wave" role="img" aria-label="Audio waveform"></div><div class="track__info"><span class="track__play"><svg width="10" height="12"><path d="M1 1l8 5-8 5z" fill="#fff"/></svg></span><div><b>Music Title here</b>Modern love song arranged for piano<br>4:02</div></div></div>
  </div>
  <div class="music__more"><a class="btn btn--light">View More</a></div>
</section>

<section class="events">
  <h2>Upcoming Events</h2>
  <div class="event-list">
    <div class="event"><div class="event__date"><b>30</b><span>Jul</span></div><div><h4>Private event – Aspendale (tbc)</h4><small>July 30 @ 2:00 pm – 5:00 pm</small><p>Solo piano for a private afternoon gathering by the bay.</p></div></div>
    <div class="event"><div class="event__date"><b>17</b><span>Aug</span></div><div><h4>Wedding Ceremony &amp; Canapes – Willow Hall</h4><small>August 17 @ 3:00 pm – 7:00 pm</small><p>Piano and cello duo for the ceremony and canapes hour.</p></div></div>
    <div class="event"><div class="event__date"><b>20</b><span>Sep</span></div><div><h4>Private event – Aspendale (tbc)</h4><small>September 20 @ 1:00 pm – 4:00 pm</small><p>Background piano music for a family celebration lunch.</p></div></div>
  </div>
  <div class="slider-dots"><i></i><i class="on"></i><i></i></div>
</section>

<section class="testimonials">
  <h2>Testimonials</h2>
  <div class="quote-badge"><svg width="24" height="20" viewBox="0 0 24 20"><path d="M0 20V11C0 4 4 1 10 0v4C6 5 5 8 5 10h5v10ZM14 20V11c0-7 4-10 10-11v4c-4 1-5 4-5 6h5v10Z" fill="#fff"/></svg></div>
  <div class="quote-box">
    We had our wedding ceremony and cocktails at a garden venue last month. After searching for a good piano player we hired Elliot after seeing reviews online, and our guests could not stop talking about the music. He was a joy to work with and gave us the perfect soundtrack to our day.
    <cite>By Author Name</cite>
  </div>
  <svg class="t-arrow t-arrow--l" width="16" height="30" viewBox="0 0 16 30"><path d="M14 2 2 15l12 13" fill="none" stroke="#999" stroke-width="2"/></svg>
  <svg class="t-arrow t-arrow--r" width="16" height="30" viewBox="0 0 16 30"><path d="M2 2l12 13L2 28" fill="none" stroke="#999" stroke-width="2"/></svg>
</section>

<footer class="footer">
  <div><h4>Quick Links</h4><ul><li>About Elliot</li><li>Events</li><li>Music</li><li>Video</li></ul></div>
  <div><h4>Sublinks</h4><ul><li>Repertoire</li><li>Prices</li><li>Gallery</li><li>Testimonials</li></ul></div>
  <div><h4>Resources</h4><ul><li>Buy CD</li><li>FAQs</li><li>Contact</li></ul></div>
  <div><h4>Follow Us</h4><div class="socials"><i></i><i></i><i></i><i></i><i></i></div><div class="brand"><span class="mark"></span>Elliot Hale</div></div>
</footer>
<div class="copyright">© 2017 Company Name. All rights reserved. Terms of Use</div>

</body>
</html>
```